〇依頼の目的
分譲地の販売に繋げたい

〇依頼内容
・ポスターサイズはB1タテです。
・ターゲット
30代~40代のファミリー層
・原稿について
添付のデータをご確認ください。
(押さえ部分と位置図程度)
基本的にはキャッチーコピー(この分譲地に住みたくなるような)を検討頂き、ビジュアル等(分譲地の写真データも添付します)で表現してください。
・アピールポイント
諏訪湖を臨む、大自然に囲まれた風光明媚な場所ですが、保育園(約300m) に近く、子育てにも適した分譲地です。
(残念ながら分譲地からは諏訪湖は見れません。。)
・その他
インパクトより分譲地のイメージが伝わる美しいデザインを希望します。
分譲地のロゴタイプもポスターに含めてご提案ください。
また、この他2つの分譲地ポスターも作成予定です。
(柿沢団地・竹原東団地)
今回採用させて頂いて案をフォーマットにして、プロジェクトにて依頼させていただくかもしれませんので、ご承知おきください。

分譲地の写真は点数が多いので、下記サイトにアップ致しました。
お手数をおかけしますが、ダウンロードにてご使用ください。
http://quillbox-share.jp/download/7c3e81a04bd92f56e1a9c07d3b28e6f41a9d5c07

それでは皆様からのご提案お待ちしております。

バランスの良いレイアウトと的確なコピーワーク・ロゴマークがとても素晴らしいです。

写真データの処理や、キャッチコピー等どれも大変洗練されており、
クオリティの高い作品をご提案頂きまして、本当にありがとうございました。
また機会を作りますので、引き続きよろしくお願いいたします。

```html
<!DOCTYPE html>
<html lang="ja">
<head>
<meta charset="utf-8">
<title>あおば台団地 分譲中</title>
<link href="https://fonts.googleapis.com/css2?family=Noto+Serif+JP:wght@400;500;700&family=Noto+Sans+JP:wght@400;700&display=swap" rel="stylesheet">
<style>
  :root {
    --sky-top: #1b74c8;
    --sky-mid: #5eaae6;
    --sky-low: #cfe6f6;
    --haze: #a9bfcf;
    --mountain: #6f8f9c;
    --hill-dark: #2e5a2c;
    --field: #7ea55a;
    --field-light: #a9c57c;
    --forest: #274d24;
    --band: rgba(255,255,255,0.88);
    --navy: #1d3c6b;
    --white: #ffffff;
    --footer-bg: #2a552a;
  }
  html, body { margin: 0; padding: 0; overflow: hidden; background: #eef3f6; }
  .poster {
    position: relative; width: 848px; height: 1200px; overflow: hidden;
    font-family: "Noto Serif JP", serif; color: var(--white);
  }
  .sky-photo {
    position: absolute; left: 0; right: 0; top: 0; height: 660px;
    background:
      radial-gradient(circle at 84% 6%, #ffffff 0, rgba(255,255,255,0.75) 7%, rgba(255,255,255,0) 26%),
      radial-gradient(ellipse at 12% 40%, rgba(255,255,255,0.55) 0, rgba(255,255,255,0) 30%),
      radial-gradient(ellipse at 88% 48%, rgba(255,255,255,0.5) 0, rgba(255,255,255,0) 28%),
      linear-gradient(180deg, var(--sky-top) 0%, var(--sky-mid) 50%, var(--sky-low) 100%);
  }
  .aerial-photo {
    position: absolute; left: 0; right: 0; top: 636px; height: 496px;
    background: linear-gradient(180deg,
      var(--haze) 0%, var(--mountain) 8%, #56786a 14%, var(--hill-dark) 24%,
      #4f7c3c 38%, var(--field) 52%, var(--field-light) 66%, #6e9450 80%, var(--forest) 100%);
  }
  .series-name {
    position: absolute; top: 22px; width: 100%; text-align: center; margin: 0;
    font-size: 17px; letter-spacing: 0.7em; font-weight: 500;
  }
  .title {
    position: absolute; top: 196px; width: 100%; text-align: center; margin: 0;
    font-size: 98px; font-weight: 500; line-height: 150px; letter-spacing: 0.08em;
    text-shadow: 0 2px 12px rgba(20,70,130,0.35);
  }
  .title .status { letter-spacing: 0.22em; padding-left: 0.22em; }
  .catch-band {
    position: absolute; top: 568px; left: 0; right: 0; height: 66px;
    background: linear-gradient(90deg, rgba(255,255,255,0) 0%, var(--band) 18%, var(--band) 82%, rgba(255,255,255,0) 100%);
  }
  .catch {
    position: absolute; top: 580px; width: 100%; text-align: center; margin: 0;
    font-size: 31px; color: var(--navy); letter-spacing: 0.2em; font-weight: 500; line-height: 42px;
  }
  .point {
    position: absolute; padding: 5px 16px; font-size: 19px; letter-spacing: 0.1em; line-height: 28px;
    border: 1.5px solid rgba(255,255,255,0.9); border-radius: 4px;
    background: rgba(25,70,110,0.3); white-space: nowrap;
  }
  .point-nature { top: 780px; left: 468px; }
  .point-city { top: 822px; left: 40px; }
  .point-school { top: 868px; left: 420px; }
  .site-pin { position: absolute; top: 1016px; left: 56px; width: 22px; height: 30px; }
  .site-label {
    position: absolute; top: 1014px; left: 84px; margin: 0; font-size: 11px;
    font-family: "Noto Sans JP", sans-serif; line-height: 1.3;
    text-shadow: 0 1px 3px rgba(0,0,0,0.5);
  }
  .site-label b { font-size: 17px; display: block; }
  .footer {
    position: absolute; left: 0; right: 0; bottom: 0; height: 68px; background: var(--footer-bg);
    font-family: "Noto Sans JP", sans-serif; display: flex; align-items: center; padding: 0 16px; box-sizing: border-box;
  }
  .org { display: flex; align-items: center; gap: 8px; }
  .org-mark { width: 16px; height: 16px; border-radius: 50%; background: var(--white); }
  .org-name { font-size: 17px; font-weight: 700; }
  .org-note { font-size: 8px; margin-top: 4px; opacity: 0.85; }
  .web { margin-left: 90px; font-size: 10px; line-height: 1.6; }
  .contact { margin-left: auto; text-align: right; font-size: 10px; }
  .tel { font-size: 27px; font-weight: 700; letter-spacing: 0.02em; line-height: 1; }
</style>
</head>
<body>
<main class="poster">
  <div class="sky-photo" role="img" aria-label="白い雲が広がる明るい青空と太陽の光"></div>
  <div class="aerial-photo" role="img" aria-label="遠くに湖と山並みを望む、緑の森と畑に囲まれた分譲地の空撮写真"></div>

  <p class="series-name">AOBADAIDANCHI</p>
  <h1 class="title">あおば台団地<br><span class="status">分譲中</span></h1>

  <div class="catch-band"></div>
  <p class="catch">家族が笑顔になる場所へ</p>

  <span class="point point-nature">自然豊かで静かな里</span>
  <span class="point point-city">市街地に近い</span>
  <span class="point point-school">学校や保育園などの施設も充実</span>

  <svg class="site-pin" viewBox="0 0 22 30" aria-hidden="true">
    <path d="M11 1C5.5 1 1 5.4 1 10.8 1 18 11 29 11 29s10-11 10-18.2C21 5.4 16.5 1 11 1z" fill="#e5483c" stroke="#fff" stroke-width="1.5"/>
    <circle cx="11" cy="10.5" r="3.6" fill="#fff"/>
  </svg>
  <p class="site-label">現地<b>あおば台団地</b></p>

  <footer class="footer">
    <div>
      <div class="org"><span class="org-mark"></span><span class="org-name">信州すまい供給公社</span></div>
      <div class="org-note">宅地建物取引業者 登録番号 第000号 所在地 県内某所</div>
    </div>
    <div class="web">ホームページ<br>www.shinshu-sumai.example.jp</div>
    <div class="contact">お問い合わせ　信州すまい供給公社<br><span class="tel">TEL.026-000-4821</span></div>
  </footer>
</main>
</body>
</html>
```